Creative Advertisements for Magazine

Require one (1) ad created for a full page, 1/3 page, 2/3 page size.

Video Monitoring Solution - we are currently creating an explainer video of this offering and I have attached the document for the video monitoring script to help you understand what we are selling. Please also watch the 1 minute overview of who we are and what we do at https://videohost.example/qWp7RzKf3Ld . The creative magazine ad should include an image of a monitoring station (could be animated) watching a crime occurring through security cameras or something like that. You will need to rewrite the below items to be effective and have a call to action.

Our monitoring station reacts immediately to emergency events or crimes in progress by talking to the intruder and/or calling the police or your contact list. Your site management can also login anytime and view the site from their phone or PC.

The security cameras, 24/7 video storage and audible speakers can be purchased or rented from The Lanternwell Depot. We install, program and monitor the system. Prices start at $175/month. Reduce Crime, Improve Site Management.

we will need our four vertical logos (as shown in the attached file and brochure) to be in the ad along with our phone numbers shown in the business card and email sales@lantdepot.example and website www.lantdepot.example. I'm hoping the general feel of the ad can match our existing feel of our brochure and attached post card.

```html
<!DOCTYPE html>
<html lang="en">
<head>
<meta charset="utf-8">
<title>The Lanternwell Depot – Video Monitoring Ad</title>
<link rel="stylesheet" href="https://fonts.googleapis.com/css2?family=Oswald:wght@700&family=Roboto:wght@300;400&family=Teko:wght@500&display=swap">
<style>
  :root {
    --navy: #1d355e;
    --orange: #e8573a;
    --paper: #ffffff;
    --backdrop: #e9e6e2;
    --ink: #2b3f63;
    --green-dark: #0f3b14;
    --green: #3aa63d;
    --photo-dark: #2c2f33;
    --photo-orange: #b4643a;
  }
  * { box-sizing: border-box; margin: 0; padding: 0; }
  html, body { width: 1200px; height: 1200px; overflow: hidden; background: var(--backdrop); }
  .ad-page {
    position: absolute; left: 160px; top: 10px; width: 880px; height: 1180px;
    background: var(--paper); box-shadow: 0 2px 10px rgba(0,0,0,.12);
  }
  .brand {
    position: absolute; left: 60px; top: 80px; width: 760px; height: 110px;
    display: flex; align-items: center; justify-content: center; gap: 24px;
  }
  .brand-square { width: 46px; height: 46px; background: var(--orange); }
  .brand-name {
    font-family: 'Oswald', sans-serif; font-weight: 700; font-size: 60px;
    color: var(--navy); text-transform: uppercase; letter-spacing: 1px; line-height: 1;
  }
  .media-grid { position: absolute; left: 40px; top: 225px; width: 775px; height: 443px; }
  .media-grid > * { position: absolute; }
  .photo-camera-wall { left: 0; top: 0; width: 465px; height: 175px;
    background: linear-gradient(135deg, #3a3c40 0%, #6f8593 55%, #2a2d31 100%); }
  .photo-night-vision { left: 0; top: 175px; width: 465px; height: 268px;
    background: linear-gradient(160deg, var(--green) 0%, #1f6d23 55%, var(--green-dark) 100%); }
  .photo-jail { left: 465px; top: 0; width: 310px; height: 230px;
    background: linear-gradient(120deg, var(--photo-dark) 0%, var(--photo-orange) 55%, #5b4a40 100%); }
  .service-panel { left: 465px; top: 230px; width: 310px; height: 213px; background: var(--navy);
    display: flex; justify-content: center; align-items: center; gap: 12px; padding-top: 10px; }
  .service { display: flex; flex-direction: column; align-items: center; gap: 6px; width: 64px; }
  .service svg { width: 60px; height: 60px; }
  .service-label { font-family: 'Teko', sans-serif; font-weight: 500; font-size: 19px; color: #fff; line-height: 1; }
  .quote { position: absolute; left: 55px; top: 718px; width: 750px; height: 150px;
    border: 4px dotted var(--navy); border-radius: 2px; padding: 20px 28px 0 32px; }
  .quote-mark { position: absolute; font-family: 'Oswald', sans-serif; font-weight: 700;
    font-size: 80px; line-height: 1; color: var(--navy); background: var(--paper); padding: 0 6px; }
  .quote-mark.open { left: -30px; top: -22px; }
  .quote-mark.close { right: -30px; bottom: -58px; }
  .quote-text { font-family: 'Roboto', sans-serif; font-weight: 300; font-size: 19px;
    line-height: 1.38; color: var(--ink); text-transform: uppercase; text-align: justify; }
  .features { position: absolute; left: 55px; top: 918px; list-style: none; }
  .features li { display: flex; align-items: center; gap: 10px; height: 36px;
    font-family: 'Roboto', sans-serif; font-weight: 400; font-size: 20px; color: var(--navy);
    text-transform: uppercase; white-space: nowrap; }
  .features svg { width: 24px; height: 24px; }
  .offer { position: absolute; left: 300px; top: 912px; width: 505px;
    font-family: 'Teko', sans-serif; font-weight: 500; font-size: 48px; line-height: 1;
    color: var(--orange); text-transform: uppercase; text-align: right; white-space: nowrap; }
  .contact-band { position: absolute; left: 0; top: 1080px; width: 880px; height: 70px;
    background: var(--orange); display: flex; align-items: center; justify-content: space-between;
    gap: 20px; padding: 6px 30px 0; font-family: 'Teko', sans-serif; font-weight: 500; font-size: 22px;
    letter-spacing: 1.5px; color: #fff; text-transform: uppercase; white-space: nowrap; }
  .contact-item { display: flex; align-items: center; gap: 8px; }
  .contact-item svg { width: 20px; height: 20px; margin-top: -5px; flex: none; }
</style>
</head>
<body>
<main class="ad-page">
  <header class="brand">
    <span class="brand-square"></span>
    <span class="brand-name">The Lanternwell Depot</span>
  </header>

  <section class="media-grid">
    <div class="photo-camera-wall" role="img" aria-label="Wall-mounted security camera beside a bank of monitoring screens"></div>
    <div class="photo-night-vision" role="img" aria-label="Night-vision camera feed of a masked intruder with a red target overlay"></div>
    <div class="photo-jail" role="img" aria-label="Person in an orange jumpsuit holding prison bars"></div>
    <div class="service-panel">
      <div class="service">
        <svg viewBox="0 0 60 60"><circle cx="30" cy="30" r="27" fill="none" stroke="#fff" stroke-width="3"/><rect x="16" y="24" width="24" height="11" rx="2" fill="#fff" transform="rotate(-15 28 30)"/><rect x="13" y="36" width="4" height="10" fill="#fff"/></svg>
        <span class="service-label">Cameras</span>
      </div>
      <div class="service">
        <svg viewBox="0 0 60 60"><circle cx="30" cy="30" r="27" fill="none" stroke="#fff" stroke-width="3"/><circle cx="37" cy="23" r="6" fill="none" stroke="#fff" stroke-width="3"/><line x1="33" y1="27" x2="17" y2="43" stroke="#fff" stroke-width="3"/><line x1="21" y1="39" x2="25" y2="43" stroke="#fff" stroke-width="3"/></svg>
        <span class="service-label">Access</span>
      </div>
      <div class="service">
        <svg viewBox="0 0 60 60"><circle cx="30" cy="30" r="27" fill="none" stroke="#fff" stroke-width="3"/><rect x="19" y="15" width="22" height="30" rx="2" fill="none" stroke="#fff" stroke-width="3"/><rect x="23" y="19" width="14" height="6" fill="#fff"/><g fill="#fff"><rect x="23" y="29" width="4" height="4"/><rect x="33" y="29" width="4" height="4"/><rect x="23" y="36" width="4" height="4"/><rect x="33" y="36" width="4" height="4"/></g></svg>
        <span class="service-label">Alarm</span>
      </div>
      <div class="service">
        <svg viewBox="0 0 60 60"><circle cx="30" cy="30" r="27" fill="none" stroke="#fff" stroke-width="3"/><path d="M16 38 h28" stroke="#fff" stroke-width="3"/><g stroke="#fff" stroke-width="3"><line x1="20" y1="22" x2="20" y2="33"/><line x1="26" y1="20" x2="26" y2="33"/><line x1="32" y1="20" x2="32" y2="33"/><line x1="38" y1="22" x2="38" y2="33"/></g></svg>
        <span class="service-label">Intercom</span>
      </div>
    </div>
  </section>

  <blockquote class="quote">
    <span class="quote-mark open">&ldquo;</span>
    <p class="quote-text">Our monitoring station reacts immediately to emergency events or crimes in progress by talking to the intruder and/or calling the police or your contact list. Your site management can also login anytime and view the site from their phone or PC.</p>
    <span class="quote-mark close">&rdquo;</span>
  </blockquote>

  <ul class="features">
    <li><svg viewBox="0 0 24 24"><rect x="2" y="5" width="17" height="17" fill="none" stroke="#e8573a" stroke-width="2"/><path d="M6 13 l4 4 l11 -14" fill="none" stroke="#e8573a" stroke-width="3"/></svg>Security Cameras</li>
    <li><svg viewBox="0 0 24 24"><rect x="2" y="5" width="17" height="17" fill="none" stroke="#e8573a" stroke-width="2"/><path d="M6 13 l4 4 l11 -14" fill="none" stroke="#e8573a" stroke-width="3"/></svg>24/7 Video Storage</li>
    <li><svg viewBox="0 0 24 24"><rect x="2" y="5" width="17" height="17" fill="none" stroke="#e8573a" stroke-width="2"/><path d="M6 13 l4 4 l11 -14" fill="none" stroke="#e8573a" stroke-width="3"/></svg>Audible Speakers</li>
  </ul>

  <p class="offer">Can be purchased or rented<br>from The Lanternwell Depot</p>

  <footer class="contact-band">
    <span class="contact-item"><svg viewBox="0 0 22 22"><rect x="1" y="4" width="20" height="14" fill="none" stroke="#fff" stroke-width="2"/><path d="M1 4 l10 8 l10 -8" fill="none" stroke="#fff" stroke-width="2"/></svg>sales@lantdepot.example</span>
    <span class="contact-item"><svg viewBox="0 0 22 22"><circle cx="11" cy="11" r="9" fill="none" stroke="#fff" stroke-width="2"/><path d="M2 11 h18 M11 2 c-5 5 -5 13 0 18 M11 2 c5 5 5 13 0 18" fill="none" stroke="#fff" stroke-width="1.5"/></svg>www.lantdepot.example</span>
    <span class="contact-item"><svg viewBox="0 0 22 22"><path d="M3 8 c0 -4 16 -4 16 0 v2 h-4 v-2 h-8 v2 h-4 z" fill="#fff"/><rect x="5" y="11" width="12" height="8" rx="1" fill="#fff"/></svg>Tollfree:877.555.0142</span>
  </footer>
</main>
</body>
</html>
```